Brightwell Power Systems

We'd like a web design that's beautiful and professional. We replace existing inefficient systems (mostly lighting at the moment but expanding) with highly efficient systems.

```html
<!DOCTYPE html>
<html lang="en">
<head>
<meta charset="utf-8">
<title>Brightwell Power Systems</title>
<link rel="stylesheet" href="https://fonts.googleapis.com/css2?family=Source+Sans+3:wght@400;600;700&display=swap">
<style>
  :root {
    --backdrop: #c4c4c4;
    --page: #ffffff;
    --edge: #1a1a1a;
    --green: #22a34f;
    --green-light: #5cb85a;
    --accent-yellow: #f2e23a;
    --band: #efefef;
    --card: #ffffff;
    --ring: #d9d9db;
    --ink: #3d3d3d;
    --ink-strong: #222222;
    --footer: #a7a8ab;
    --footer-text: #e6e6e6;
    --footer-line: #d4d4d6;
  }
  * { box-sizing: border-box; margin: 0; padding: 0; }
  html, body {
    width: 1200px; height: 959px; overflow: hidden;
    background: var(--backdrop);
    font-family: "Source Sans 3", "Myriad Pro", Arial, sans-serif;
  }
  .canvas { position: relative; width: 1200px; height: 959px; }
  .page {
    position: absolute; left: 157px; top: 0; width: 880px; height: 959px;
    background: var(--page);
    border-left: 2px solid var(--edge); border-right: 2px solid var(--edge);
    overflow: hidden;
  }
  .page > * { position: absolute; }

  /* header */
  .brand {
    left: 5px; top: 6px; width: 133px; height: 106px;
    background: var(--page); border: 2px solid var(--edge);
    display: flex; align-items: center; justify-content: center;
    text-align: center; padding: 8px;
    color: var(--green); font-weight: 700; font-size: 17px; line-height: 1.15;
    z-index: 2;
  }
  .search { left: 684px; top: 11px; display: flex; }
  .search-field {
    width: 110px; height: 28px; border: 1px solid #cfcfcf; border-radius: 3px 0 0 3px;
    font-size: 14px; color: #8a8a8a; padding: 4px 8px; background: #fafafa;
  }
  .search-button {
    width: 40px; height: 28px; background: var(--green); border-radius: 0 3px 3px 0;
    display: flex; align-items: center; justify-content: center;
  }
  .nav {
    left: 136px; top: 52px; width: 742px; height: 68px; background: var(--green);
  }
  .nav a {
    position: absolute; top: 0; height: 68px; line-height: 64px;
    color: #fff; text-decoration: none; font-size: 21px; font-weight: 600;
    text-align: center;
  }
  .nav .is-active {
    left: 240px; width: 138px; background: var(--green-light);
    border-bottom: 6px solid var(--accent-yellow);
  }
  .nav .nav-contact { left: 450px; width: 90px; }
  .nav .nav-faq { left: 600px; width: 70px; }

  /* hero */
  .hero-visual {
    left: 110px; top: 150px; width: 195px; height: 260px;
    border-radius: 45% 45% 30% 30%;
    background: radial-gradient(ellipse at 45% 40%, #f4f4f4 0%, #d6d6d6 45%, #a7a7a7 75%, #ffffff 100%);
  }
  .hero-heading {
    left: 374px; top: 162px; color: var(--ink); font-weight: 400;
    font-size: 31px; line-height: 36px;
  }
  .hero-heading span { display: block; }
  .hero-heading .second { padding-left: 89px; }
  .slider-controls { left: 751px; top: 378px; display: flex; gap: 2px; }
  .slider-controls span {
    width: 26px; height: 35px; background: var(--green);
    display: flex; align-items: center; justify-content: center;
  }
  .slider-controls span:first-child { border-radius: 5px 0 0 5px; }
  .slider-controls span:last-child { border-radius: 0 5px 5px 0; }

  /* features */
  .features { left: 0; top: 437px; width: 876px; height: 316px; background: var(--band); }
  .feature {
    position: absolute; top: 75px; width: 181px; height: 172px;
    background: var(--card); border-radius: 10px; text-align: center;
    padding: 38px 14px 0;
  }
  .feature:nth-child(1) { left: 110px; }
  .feature:nth-child(2) { left: 346px; }
  .feature:nth-child(3) { left: 579px; }
  .feature-icon {
    position: absolute; left: 50%; top: -75px; width: 94px; height: 94px;
    margin-left: -47px; border-radius: 50%; background: var(--ring);
    display: flex; align-items: center; justify-content: center;
  }
  .feature-icon .art {
    width: 74px; height: 74px; border-radius: 50%; border: 5px solid #fff;
  }
  .art-rebates { background: linear-gradient(135deg, #e9d8c6, #a5694c); }
  .art-retrofit { background: linear-gradient(135deg, #d8d4c6, #8f8a78); }
  .art-tax { background: linear-gradient(135deg, #f0e6d4, #9b6b3c); }
  .feature h2 {
    font-size: 18px; font-weight: 700; color: var(--ink-strong); margin-bottom: 10px; white-space: nowrap;
  }
  .feature p {
    font-size: 15px; line-height: 19px; color: var(--ink); text-align: left; padding-left: 12px;
  }

  /* footer */
  .footer { left: 0; top: 753px; width: 876px; height: 206px; background: var(--footer); }
  .footer-links {
    position: absolute; left: 30px; top: 30px; width: 462px; height: 33px;
    border-bottom: 2px solid var(--footer-line);
  }
  .footer-links a {
    position: absolute; top: 0; color: var(--footer-text); text-decoration: none;
    font-size: 18px; font-weight: 600;
  }
  .footer-links a:nth-child(1) { left: 17px; }
  .footer-links a:nth-child(2) { left: 191px; }
  .footer-links a:nth-child(3) { left: 372px; }
  .copyright {
    position: absolute; right: 27px; bottom: 14px; color: var(--footer-text);
    font-size: 17px; font-weight: 600;
  }
</style>
</head>
<body>
<div class="canvas">
  <div class="page">
    <div class="brand">Brightwell Power Systems</div>

    <div class="search">
      <div class="search-field">Search..</div>
      <div class="search-button">
        <svg width="18" height="18" viewBox="0 0 18 18" aria-hidden="true">
          <circle cx="7.5" cy="7.5" r="5" fill="none" stroke="#fff" stroke-width="2.4"/>
          <line x1="11" y1="11" x2="16" y2="16" stroke="#fff" stroke-width="2.6" stroke-linecap="round"/>
        </svg>
      </div>
    </div>

    <nav class="nav">
      <a class="is-active" href="#">Services</a>
      <a class="nav-contact" href="#">Contact</a>
      <a class="nav-faq" href="#">FAQ</a>
    </nav>

    <div class="hero-visual" role="img" aria-label="LED spot lamp with clear lens and silver base"></div>
    <h1 class="hero-heading">
      <span>Led for every application</span>
      <span class="second">Change to LED now</span>
    </h1>
    <div class="slider-controls">
      <span><svg width="12" height="16" viewBox="0 0 12 16" aria-hidden="true"><polyline points="9,2 3,8 9,14" fill="none" stroke="#fff" stroke-width="2.6"/></svg></span>
      <span><svg width="12" height="16" viewBox="0 0 12 16" aria-hidden="true"><polyline points="3,2 9,8 3,14" fill="none" stroke="#fff" stroke-width="2.6"/></svg></span>
    </div>

    <section class="features">
      <article class="feature">
        <div class="feature-icon"><div class="art art-rebates" role="img" aria-label="Hand holding coins and banknotes"></div></div>
        <h2>Utility Rebates</h2>
        <p>Many companies offer either a direct rebate or credit to your utility account</p>
      </article>
      <article class="feature">
        <div class="feature-icon"><div class="art art-retrofit" role="img" aria-label="Money bag marked with a dollar sign"></div></div>
        <h2>LED retrofit process</h2>
        <p>Many companies offer either a direct rebate or credit to your utility account</p>
      </article>
      <article class="feature">
        <div class="feature-icon"><div class="art art-tax" role="img" aria-label="Tax form with pen and calculator"></div></div>
        <h2>Tax Incentives</h2>
        <p>Many companies offer either a direct rebate or credit to your utility account</p>
      </article>
    </section>

    <footer class="footer">
      <div class="footer-links">
        <a href="#">Services</a>
        <a href="#">Contact</a>
        <a href="#">FAQ</a>
      </div>
      <div class="copyright">Copyright Brightwell Power Systems Inc</div>
    </footer>
  </div>
</div>
</body>
</html>
```